Paul Sefton Personal Card

I am looking for a personal card that has my contact information on the front and then the url for my website on the back. I am a fan of minimal, modern design, but am very open minded to other styles. Both portrait and landscape designs are acceptable. The only other specification that I have is that some sort of graphic of a raven is present somewhere on the card (my last name 'Sefton' means raven in German).
Contact Information for Business Card
Paul Sefton
608.554.1893
paulwsefton@postvane.net
paulwsefton.com
Colors
Designer to choose colors to be used in the design.
Requirements
Must have
- Raven on some part of the card

```html
<!DOCTYPE html>
<html lang="en">
<head>
<meta charset="utf-8">
<title>Paul Sefton Personal Card</title>
<link rel="stylesheet" href="https://fonts.googleapis.com/css2?family=Nunito:wght@300;400;700;800&family=Open+Sans:wght@400&display=swap">
<style>
  :root {
    --backdrop: #5b4a38;
    --card-dark: #060708;
    --card-glow: #232527;
    --card-light: #ffffff;
    --ink: #1d1d1f;
    --ink-soft: #2a2a2c;
    --url-text: #f4f4f4;
    --raven-tone: #030404;
  }
  html, body {
    margin: 0;
    padding: 0;
    width: 1200px;
    height: 1000px;
    overflow: hidden;
    background: var(--backdrop);
  }
  .canvas {
    position: relative;
    width: 1200px;
    height: 1000px;
  }
  .card {
    position: absolute;
    top: 175px;
    width: 407px;
    height: 683px;
    border-radius: 30px;
    overflow: hidden;
  }
  .card--back {
    left: 162px;
    background: radial-gradient(ellipse 58% 42% at 50% 52%, var(--card-glow) 0%, #141516 50%, var(--card-dark) 88%);
  }
  .card--front {
    left: 570px;
    background: var(--card-light);
  }
  .raven-art {
    position: absolute;
    left: 30px;
    top: 280px;
    width: 350px;
    height: 120px;
    border-radius: 50%;
    transform: rotate(28deg);
    background: radial-gradient(ellipse at 50% 50%, var(--raven-tone) 0%, var(--raven-tone) 45%, rgba(3,4,4,0.5) 65%, rgba(3,4,4,0) 72%);
  }
  .site-url {
    position: absolute;
    left: 0;
    right: 0;
    top: 626px;
    text-align: center;
    font-family: "Open Sans", sans-serif;
    font-size: 22px;
    color: var(--url-text);
    letter-spacing: 0.2px;
  }
  .contact {
    position: absolute;
    right: 30px;
    top: 526px;
    text-align: right;
  }
  .contact__name {
    margin: 0 0 32px 0;
    font-family: "Nunito", sans-serif;
    font-weight: 800;
    font-size: 28px;
    line-height: 1.25;
    color: var(--ink);
    letter-spacing: 0.3px;
  }
  .contact__line {
    display: flex;
    justify-content: flex-end;
    align-items: center;
    gap: 7px;
    height: 27px;
    font-family: "Nunito", sans-serif;
    font-weight: 300;
    font-size: 19px;
    color: var(--ink-soft);
  }
  .contact__icon {
    width: 21px;
    height: 21px;
    flex: none;
  }
</style>
</head>
<body>
  <main class="canvas">
    <section class="card card--back" aria-label="Card back">
      <div class="raven-art" role="img" aria-label="Dark silhouette of a raven in flight, wings spread diagonally"></div>
      <div class="site-url">paulwsefton.com</div>
    </section>

    <section class="card card--front" aria-label="Card front">
      <div class="contact">
        <h1 class="contact__name">Paul Sefton</h1>
        <div class="contact__line">
          <span>608.554.1893</span>
          <svg class="contact__icon" viewBox="0 0 21 21" aria-hidden="true">
            <circle cx="10.5" cy="10.5" r="10.5" fill="#1d1d1f"/>
            <rect x="7" y="4.5" width="7" height="12" rx="1.2" fill="none" stroke="#fff" stroke-width="1.4"/>
            <line x1="8.5" y1="14" x2="12.5" y2="14" stroke="#fff" stroke-width="1.2"/>
          </svg>
        </div>
        <div class="contact__line">
          <span>paulwsefton@postvane.net</span>
          <svg class="contact__icon" viewBox="0 0 21 21" aria-hidden="true">
            <circle cx="10.5" cy="10.5" r="10.5" fill="#1d1d1f"/>
            <rect x="5" y="6.5" width="11" height="8" rx="1" fill="#fff"/>
            <polyline points="5.3,7 10.5,11.2 15.7,7" fill="none" stroke="#1d1d1f" stroke-width="1.2"/>
          </svg>
        </div>
      </div>
    </section>
  </main>
</body>
</html>
```